Webdesign für KFZ-Service-Betrieb
Zielgruppe
Wartung, Reparatur und Instandsetzung von Kraftfahrzeugen aller Marken.
Reifenhandel, Old- und Youngtimer-Service, An- und Verkauf von Fahrzeugen.
Aufgabenstellung
Firmenfarbe ist blau.
Moderner, Übersichtlicher und Transparenter Auftritt erwünscht.

```html
<!DOCTYPE html>
<html lang="de">
<head>
<meta charset="utf-8">
<title>Wir über uns – KFZ-Service</title>
<link rel="stylesheet" href="https://fonts.googleapis.com/css2?family=Old+Standard+TT:wght@400;700&family=Open+Sans:wght@600&display=swap">
<style>
  :root {
    --brand-blue: #1f2b96;
    --lavender: #7f88c6;
    --white: #ffffff;
    --ink: #111111;
    --black: #000000;
    --serif: "Old Standard TT", "Times New Roman", serif;
    --sans: "Open Sans", Arial, sans-serif;
  }
  * { box-sizing: border-box; margin: 0; padding: 0; }
  html, body { width: 1200px; height: 2396px; overflow: hidden; background: var(--white); }
  .page { position: relative; width: 1200px; height: 2396px; font-family: var(--serif); }

  .logo-box {
    position: absolute; left: 27px; top: 30px; width: 114px; height: 110px;
    border: 3px solid var(--brand-blue); color: var(--brand-blue);
    font-family: var(--sans); font-weight: 600; font-size: 23px; letter-spacing: 3px;
    line-height: 29px; padding: 11px 0 0 15px;
  }
  .page-title {
    position: absolute; left: 0; right: 0; top: 82px; text-align: center; padding-left: 20px;
    font-family: var(--sans); font-weight: 600; font-size: 28px; letter-spacing: 5px;
    color: var(--brand-blue);
  }

  .tile { position: absolute; overflow: hidden; }
  .photo { position: absolute; }

  .text-tile {
    display: flex; flex-direction: column; align-items: center; justify-content: center;
    text-align: center; padding: 0 8px;
  }
  .text-tile h2 {
    font-family: var(--serif); font-weight: 700; font-size: 31px; line-height: 40px;
    text-transform: uppercase; letter-spacing: 0.5px; margin-bottom: 10px;
  }
  .text-tile p { font-size: 17px; line-height: 21.5px; }

  .on-white { background: var(--white); color: var(--brand-blue); }
  .on-white p { color: var(--ink); }
  .on-blue { background: var(--brand-blue); color: var(--white); }
  .on-lavender { background: var(--lavender); color: var(--white); }
  .on-plain { background: var(--white); color: var(--ink); }

  .slider-nav { position: absolute; left: 515px; top: 681px; display: flex; }
  .slider-nav span { width: 42px; height: 39px; display: flex; align-items: center; justify-content: center; }
  .slider-nav .prev { background: var(--white); }
  .slider-nav .next { background: var(--black); }

  .read-more {
    display: inline-block; margin-top: 38px; background: var(--black); color: var(--white);
    font-family: var(--serif); font-weight: 700; font-size: 21px; padding: 13px 34px;
  }

  .contact {
    position: absolute; left: 0; top: 1812px; width: 1200px; height: 584px;
    background: radial-gradient(ellipse at 70% 40%, #4a5063 0%, #2d3140 45%, #1a1d27 100%);
    color: var(--white); text-align: center;
  }
  .contact h2 {
    position: absolute; left: 0; right: 0; top: 40px;
    font-family: var(--serif); font-weight: 700; font-size: 68px; line-height: 84px; letter-spacing: 1px;
  }
  .contact .hours { position: absolute; left: 0; right: 0; top: 226px; font-size: 17px; line-height: 28px; font-weight: 700; }
  .contact .phones { position: absolute; left: 460px; top: 360px; display: flex; align-items: center; gap: 18px; }
  .contact .phones p { font-size: 20px; line-height: 28px; font-weight: 700; text-align: left; letter-spacing: 1px; }
</style>
</head>
<body>
<div class="page">
  <div class="logo-box">YOUR<br>LOGO<br>HERE</div>
  <h1 class="page-title">Wir über uns</h1>

  <div class="photo" style="left:0;top:158px;width:600px;height:562px;background:linear-gradient(160deg,#6b6b6b,#2e2e2e 60%,#8a7f74);" role="img" aria-label="Bronzefarbener Sportwagen auf einer Rennstrecke vor einer Tribüne"></div>
  <div class="slider-nav">
    <span class="prev"><svg width="14" height="22" viewBox="0 0 14 22"><path d="M12 2 L3 11 L12 20" fill="none" stroke="#000" stroke-width="3"/></svg></span>
    <span class="next"><svg width="14" height="22" viewBox="0 0 14 22"><path d="M2 2 L11 11 L2 20" fill="none" stroke="#fff" stroke-width="3"/></svg></span>
  </div>
  <div class="photo" style="left:600px;top:158px;width:600px;height:281px;background:linear-gradient(180deg,#c9d3e6,#3a4a8c 60%,#1c1f2b);" role="img" aria-label="Zwei Mechaniker in blauen Overalls an einem Auto mit geöffneter Motorhaube"></div>
  <div class="tile text-tile on-white" style="left:600px;top:439px;width:281px;height:281px;">
    <h2>Pro<br>Solutions</h2>
    <p>loremp loremp loremp lorem lormel<br>lorem loremp loremp loremp loore<br>loremp loremp loremp</p>
  </div>
  <div class="photo" style="left:881px;top:439px;width:319px;height:281px;background:linear-gradient(135deg,#8a8f98,#6e5a33 50%,#3a3f4c);" role="img" aria-label="Hände eines Mechanikers an einem offenen Motorblock"></div>

  <div class="tile text-tile on-lavender" style="left:0;top:720px;width:598px;height:276px;">
    <h2>Reparatur und<br>Instandsetzung</h2>
    <p>loremp loremp loremp lorem lormel loremp lorem lorem lorem lorem<br>lorem loremp loremp loremp loore lorem lorem &nbsp;lorem lorem lorem<br>loremp loremp loremp loremp loremp lorem lorem</p>
  </div>
  <div class="photo" style="left:598px;top:720px;width:283px;height:276px;background:linear-gradient(160deg,#b8c2d6,#2b3a7a 55%,#222);" role="img" aria-label="Mechaniker mit Klemmbrett im Gespräch mit einer Kundin in der Werkstatt"></div>
  <div class="tile text-tile on-blue" style="left:881px;top:720px;width:319px;height:276px;">
    <h2>Wartung</h2>
    <p>loremp loremp loremp lorem lormel<br>lorem loremp loremp loremp loore<br>loremp loremp loremp</p>
  </div>

  <div class="tile text-tile on-plain" style="left:0;top:996px;width:598px;height:541px;justify-content:flex-start;padding-top:52px;">
    <h2>An- und Verkauf<br>von Fahrzeugen</h2>
    <p>loremp loremp loremp lorem lormel loremp lorem lorem lorem lorem<br>lorem loremp loremp loremp loore lorem lorem &nbsp;lorem lorem lorem<br>loremp loremp loremp loremp loremp lorem lorem &nbsp;loremp loremp<br>lorem loremp lorem lorem lorem lorem lorem loremp loremp loremp<br>loremp loremp lorem lorem &nbsp;loremp loremplorem loremp lorem lorem<br>lorem lorem loremloremp loremp loremp loremp loremp lorem lorem<br>loremp loremplorem loremp lorem lorem lorem lorem loremloremp<br>loremp loremp loremp loremp lorem lorem &nbsp;loremp loremp<br>lorem loremp lorem lorem lorem lorem lorem</p>
    <span class="read-more">Read more</span>
  </div>
  <div class="tile text-tile on-blue" style="left:598px;top:996px;width:283px;height:281px;justify-content:flex-start;padding-top:80px;">
    <h2 style="white-space:nowrap;">Reifenhandel</h2>
    <p>loremp loremp loremp lorem lormel<br>lorem loremp loremp loremp loore<br>loremp loremp loremp</p>
  </div>
  <div class="photo" style="left:881px;top:996px;width:319px;height:281px;background:linear-gradient(150deg,#f2f2f2,#555 45%,#222);" role="img" aria-label="Reihe von Autoreifen auf einer Straße"></div>
  <div class="photo" style="left:598px;top:1277px;width:602px;height:260px;background:linear-gradient(180deg,#9a9da6,#3c3f46 50%,#d8d8d8);" role="img" aria-label="Dunkelgraue Oberklasse-Limousine in Seitenansicht"></div>

  <div class="photo" style="left:0;top:1537px;width:598px;height:275px;background:linear-gradient(180deg,#3a3a3a,#9a9a9a 55%,#6a6a6a);" role="img" aria-label="Schwarz-weißes Foto eines klassischen Cabriolets mit Brautpaar"></div>
  <div class="tile text-tile on-blue" style="left:598px;top:1537px;width:602px;height:275px;">
    <h2>An- und Verkauf<br>von Fahrzeugen</h2>
    <p>loremp loremp loremp lorem lormel loremp lorem lorem lorem lorem<br>lorem loremp loremp loremp loore lorem lorem &nbsp;lorem lorem lorem<br>loremp loremp loremp loremp loremp lorem lorem &nbsp;loremp loremp<br>lorem loremp lorem lorem lorem lorem lorem loremp loremp loremp<br>loremp loremp lorem lorem &nbsp;loremp loremplorem loremp lorem lorem</p>
  </div>

  <section class="contact" role="img" aria-label="Abgedunkelter Hintergrund: Motorraum und Mechaniker im Gespräch mit einer Kundin">
    <h2>OUR<br>CONTACT</h2>
    <div class="hours">
      <p>Öffnungszeiten:</p>
      <p>Mo.-Fr.: 07.30 Uhr - 18.00 Uhr</p>
      <p>Sa.: 09.00 Uhr-12.00 Uhr</p>
    </div>
    <div class="phones">
      <svg width="52" height="52" viewBox="0 0 24 24"><path fill="#fff" d="M6.6 10.8c1.4 2.8 3.8 5.1 6.6 6.6l2.2-2.2c.3-.3.7-.4 1-.2 1.1.4 2.3.6 3.6.6.6 0 1 .4 1 1V20c0 .6-.4 1-1 1C10.6 21 3 13.4 3 4c0-.6.4-1 1-1h3.5c.6 0 1 .4 1 1 0 1.3.2 2.5.6 3.6.1.3 0 .7-.2 1L6.6 10.8z"/></svg>
      <div>
        <p>800-1234-5670</p>
        <p>800-1234-5671</p>
      </div>
    </div>
  </section>
</div>
</body>
</html>
```